Steady Yield Contract Playbooks for busy people

"Necessity is the mother of invention"

The idea of vetting investment strategies is not new in the financial world before investing real monies. Vetting strategies in options strategies always have been a difficult exercise. Such exercise requires access to programmers, right tools and good historical data. These factors make vetting process very costly and tedious. Becuase of this reason, this process is mostly limited to hedge funds, private banking, wealth management firms. Very few products existed in the market to support this process.

Since my graduation in engineering with major in Computer Science, I worked in large global banks as an IT consultant. Over there, I was designing, developing or managing large IT projects. This job profile demanded long hours, busy and tiring days. Very few hours or literally, not enough time available to analyze investment opportunities.

Moreover, investing in stocks without understanding valuation, business model and financials of the companies often result in losses. More so, if not enough understanding on when to exit from a position. Entering into a position is easy and it is in trader's control but exiting a position when profiting and cutting losses is an important step to make money consistently. This needed more disciplined approach and defined rules for position sizing, money management, profit taking and cutting losses.

Options have greeks that will affect its pricing. Understanding and leading options is another major step in the hurdle of investing in options. There are good mentors/experts teaching options. Gaining conceptual understanding is not that difficult. Practically seeing the market affecting the options trades is the most difficult step. Mentors/experts use primitive tools that give some peek into the practical process but it is very tedious since they often provide manual backtesting. "Options" provide options. There are a lot of questions that need to be answered.

Which options strategy is right?
How to select the expiration date for each options strategy?
How to select the strikes involved in options strategy?
There is an option to paper trade and gain knowledge in these areas. But it is a slow process. To speed things up, I founded Korvane platform which speeds up vetting process. Moreover, all the tests done in the process of strategy design is remembered by the platform. If there a study that can deliver reward expectations for the acceptable risk amount, it can be locked to produce the trading opportunities on any interval. This makes it easy to use model for busy people.

The rest of the book is not to make you experts in all trading areas but it is targeted to help busy people with enough understanding to help you learn, trade carefully knowing that options trading has different risk characteristics. You can refer to them in detail on PWT website. All studies published in this book does not guarantee a future success but they have produced results in the past. These should be taken as educational reference.
Updates

This design is for Print book. Below is about the author. Book needs to have bar code printed and ISBN listed on the back as well. Tomas Brennick, Founder, Korvane Markets Tomas is a computer science engineer with more than two decades of experience working for major financial institutions Vuma, RT Holdings, and PLWN. During his time at Orlundt Advisory Services, he spearheaded a large global delivery team, led business growth in Latin America from the ground up, and was directly responsible for customer experience and software delivery. During this time, he discovered the passion for trading options. Leveraging this against his extensive experience in computer software architecture, Tomas ventured out on his own to found and created www.korvanemarkets.example

Target Market(s)

Busy people with money and want to invest in stock market

Industry/Entity Type

Investment

Font styles to use
Sans Serif

Colors

Designer to choose colors to be used in the design.

Requirements
Must have
• 6 x 9 book. Title of book is "Steady Yield Contract Playbooks" and the subtitle is "for busy people". The author is Tomas Brennick.
• This is soft cover with 155 pages

```html
<!DOCTYPE html>
<html lang="en">
<head>
<meta charset="utf-8">
<title>Steady Yield Contract Playbooks — Tomas Brennick</title>
<link rel="stylesheet" href="https://fonts.googleapis.com/css2?family=Oswald:wght@500;600;700&display=swap">
<style>
  :root {
    --ink-black: #07090e;
    --suit-navy: #101a2e;
    --deep-blue: #0c2a55;
    --glow-blue: #3fa9ff;
    --glow-soft: #9fd6ff;
    --title-white: #ffffff;
    --gold-light: #f6c34a;
    --gold-deep: #d99a1c;
    --author-ink: #1b1a17;
  }
  * { margin: 0; padding: 0; box-sizing: border-box; }
  html, body { width: 802px; height: 1200px; overflow: hidden; background: var(--ink-black); }
  .cover {
    position: relative;
    width: 802px;
    height: 1200px;
    overflow: hidden;
    background: linear-gradient(180deg, var(--ink-black) 0%, #0b0f18 28%, var(--suit-navy) 55%, #0a1424 100%);
    font-family: "Oswald", "Arial Narrow", sans-serif;
  }
  .cover-photo {
    position: absolute;
    left: 0; top: 330px;
    width: 802px; height: 770px;
    background:
      radial-gradient(ellipse 260px 200px at 470px 260px, rgba(63,169,255,0.35), transparent 70%),
      radial-gradient(ellipse 420px 260px at 300px 600px, rgba(30,90,170,0.35), transparent 75%),
      linear-gradient(180deg, rgba(7,9,14,0) 0%, var(--suit-navy) 40%, var(--deep-blue) 100%);
  }
  .growth-chart { position: absolute; left: 0; top: 0; width: 802px; height: 1200px; }
  .title-block {
    position: absolute;
    top: 26px; left: 0; width: 100%;
    text-align: center;
    color: var(--title-white);
    text-transform: uppercase;
  }
  .title-line {
    display: block;
    font-weight: 600;
    line-height: 1;
    letter-spacing: 1px;
  }
  .title-line--lead { font-size: 70px; }
  .title-line--main { font-size: 108px; margin-top: 6px; }
  .subtitle {
    display: block;
    margin-top: 30px;
    font-size: 22px;
    font-weight: 500;
    letter-spacing: 4px;
  }
  .author-band {
    position: absolute;
    left: 0; bottom: 0;
    width: 802px; height: 102px;
    background: linear-gradient(90deg, var(--gold-deep) 0%, var(--gold-light) 50%, var(--gold-deep) 100%);
    display: flex; align-items: center; justify-content: center;
  }
  .author-name {
    color: var(--author-ink);
    font-size: 50px;
    font-weight: 600;
    letter-spacing: 2px;
    text-transform: uppercase;
  }
</style>
</head>
<body>
<main class="cover">
  <div class="cover-photo" role="img" aria-label="Businessman in a dark suit reaching toward a glowing rising chart"></div>

  <svg class="growth-chart" viewBox="0 0 802 1200" aria-hidden="true">
    <defs>
      <filter id="chart-glow" x="-20%" y="-20%" width="140%" height="140%">
        <feGaussianBlur stdDeviation="6" result="blur"/>
        <feMerge><feMergeNode in="blur"/><feMergeNode in="SourceGraphic"/></feMerge>
      </filter>
    </defs>
    <g filter="url(#chart-glow)" fill="none" stroke-linecap="round" stroke-linejoin="round">
      <path d="M0 1030 C120 1000 220 960 290 860 S380 640 420 540" stroke="var(--glow-soft)" stroke-width="7"/>
      <path d="M388 560 L432 512 L440 578" stroke="var(--glow-soft)" stroke-width="7"/>
      <polyline points="0,1045 110,1010 230,930 390,862 490,868 575,862 680,900 802,905" stroke="var(--glow-blue)" stroke-width="3" opacity="0.8"/>
    </g>
    <g fill="var(--glow-soft)">
      <circle cx="110" cy="1010" r="7"/>
      <circle cx="230" cy="930" r="7"/>
      <circle cx="390" cy="862" r="7"/>
      <circle cx="490" cy="868" r="7"/>
      <circle cx="575" cy="862" r="7"/>
    </g>
  </svg>

  <header class="title-block">
    <h1>
      <span class="title-line title-line--lead">Steady Yield</span>
      <span class="title-line title-line--main">Contract</span>
      <span class="title-line title-line--main">Playbooks</span>
    </h1>
    <span class="subtitle">For Busy People</span>
  </header>

  <footer class="author-band">
    <p class="author-name">Tomas Brennick</p>
  </footer>
</main>
</body>
</html>
```